Business Card Design Project

We are a construction company in Orange County, CA. We need a two sided business card. We would like the back to be our logo with web URL. Front should included Name, title, address, phone, fax and email address.

our address is
627 West Marrow Blvd, Suite 305
Brenmoor, CA 90417

Our logo files are attached.

Construction

```html
<!DOCTYPE html>
<html lang="en">
<head>
<meta charset="utf-8">
<title>Halder Business Card</title>
<link rel="stylesheet" href="https://fonts.googleapis.com/css2?family=Open+Sans:wght@400;700&display=swap">
<style>
  :root {
    --stage: #e9e6e1;
    --card: #ffffff;
    --brand-blue: #1a4a7f;
    --ink-white: #ffffff;
    --card-shadow: rgba(0, 0, 0, 0.25);
  }
  * { margin: 0; padding: 0; box-sizing: border-box; }
  html, body { width: 1200px; height: 431px; overflow: hidden; }
  body {
    background: var(--stage);
    font-family: "Open Sans", Arial, sans-serif;
    position: relative;
  }
  .card {
    position: absolute;
    width: 539px;
    height: 307px;
    border-radius: 14px;
    background: var(--card);
    overflow: hidden;
    box-shadow: 0 3px 8px var(--card-shadow);
  }
  .card--front { left: 47px; top: 64px; }
  .card--back { left: 615px; top: 60px; }

  .front-band {
    position: absolute;
    left: 0; right: 0; top: 124px; bottom: 0;
    background: var(--brand-blue);
  }
  .front-logo-plate {
    position: absolute;
    left: 36px; top: 90px;
    width: 268px; height: 68px;
    background: var(--card);
  }
  .wordmark {
    position: absolute;
    color: var(--brand-blue);
    font-weight: 700;
    letter-spacing: -1px;
    line-height: 1;
    white-space: nowrap;
  }
  .front-logo-plate .wordmark {
    left: 10px; top: 3px;
    font-size: 56px;
  }
  .person {
    position: absolute;
    left: 0; width: 346px; top: 225px;
    text-align: center;
    color: var(--ink-white);
  }
  .person-name { font-size: 16px; font-weight: 700; letter-spacing: 0.2px; }
  .person-title { font-size: 13px; margin-top: 1px; }

  .contact-list {
    position: absolute;
    left: 350px; top: 136px;
    list-style: none;
    color: var(--ink-white);
    font-size: 14px;
  }
  .contact-list li {
    display: flex;
    align-items: center;
    height: 18px;
  }
  .contact-list svg {
    width: 11px; height: 11px;
    margin-right: 8px;
    fill: var(--ink-white);
    flex: none;
  }
  .address {
    position: absolute;
    left: 352px; top: 220px;
    color: var(--ink-white);
    font-size: 14px;
    line-height: 17.5px;
    font-style: normal;
  }

  .card--back .wordmark {
    left: 0; right: 0; top: 113px;
    text-align: center;
    font-size: 64px;
  }
  .back-url {
    position: absolute;
    left: 0; right: 0; top: 208px;
    text-align: center;
    color: var(--brand-blue);
    font-size: 14px;
    letter-spacing: 2.5px;
  }
</style>
</head>
<body>
  <section class="card card--front" aria-label="Business card front">
    <div class="front-band"></div>
    <div class="front-logo-plate">
      <span class="wordmark">HALDER</span>
    </div>

    <div class="person">
      <p class="person-name">YOUR NAME</p>
      <p class="person-title">Title</p>
    </div>

    <ul class="contact-list">
      <li>
        <svg viewBox="0 0 12 12" aria-hidden="true"><path d="M2.5 0.8 4.3 3.1 3.3 4.4C3.9 5.9 5.1 7.2 6.6 7.8L7.9 6.8 10.2 8.5 9.3 10.6C5 10.8 0.6 6.4 0.9 1.8Z"/></svg>
        0246813579
      </li>
      <li>
        <svg viewBox="0 0 12 12" aria-hidden="true"><path d="M3 1h6v3H3z M1 4.5h10v4.5H9V7H3v2H1z M3.5 7.5h5V11h-5z"/></svg>
        0246813579
      </li>
      <li>
        <svg viewBox="0 0 12 12" aria-hidden="true"><path d="M0.5 2.5h11v7h-11z" /><path d="M0.5 2.5 6 6.5 11.5 2.5" fill="none" stroke="#1a4a7f" stroke-width="1"/></svg>
        info@halderbuild.com
      </li>
      <li>
        <svg viewBox="0 0 12 12" aria-hidden="true"><circle cx="6" cy="6" r="5.2" fill="none" stroke="#fff" stroke-width="1.2"/><ellipse cx="6" cy="6" rx="2.2" ry="5.2" fill="none" stroke="#fff" stroke-width="1"/><path d="M1 6h10" stroke="#fff" stroke-width="1"/></svg>
        www.halderbuild.com
      </li>
    </ul>

    <address class="address">
      627 West Marrow Blvd<br>
      Suite 305<br>
      Brenmoor, CA 90417
    </address>
  </section>

  <section class="card card--back" aria-label="Business card back">
    <span class="wordmark">HALDER</span>
    <p class="back-url">www.halderbuild.com</p>
  </section>
</body>
</html>
```